Training Course Info Brochure

Hi there, I'm looking for a design for A4 Flyer (2-3 pages) on our new Course - Infection Control. I have included a previous brochure on our courses so the designed can see the look and feel we are looking for.

As this is about Infection Control, I would also like to see some RED in the design or wording.

The brochure will need to include quite a few industry/ government logos as well and graphics are important. I have included some (Health Care Industry workers) and am also open to other graphics.

Thanks for considering!

Target Market(s)

The Health profession and students wanting to work in the health field

Industry/Entity Type

Health Care

Font styles to use
Sans Serif

Colors
3277b5
f78f20
ffffff
ec1f27

Requirements
Must have
• Similar feel to the brochure I have included in this brief.

SOME RED lettering as we are teaching Infection Control during the COVID19 pandemic
Nice to have
• Lovely design with quite a few photos graphics

Company details:

Harcourt Academy of Learning
RTO 73846
FREECALL : 1800 472 913
www.harcourtlearning.edu.au
info@harcourtlearning.edu.au

```html
<!DOCTYPE html>
<html lang="en">
<head>
<meta charset="utf-8">
<title>Infection Control – Course Brochure</title>
<link href="https://fonts.googleapis.com/css2?family=Fira+Sans:ital,wght@0,300;0,400;0,600;0,700;1,400;1,600;1,700&display=swap" rel="stylesheet">
<style>
:root{
  --board:#58595d;
  --paper:#ffffff;
  --ink:#333333;
  --red:#ec1f27;
  --blue:#3277b5;
  --navy:#1f6c9e;
  --mist:#ededed;
  --tint-blue:#dfe9f3;
  --tint-red:#fbe1e2;
  --tint-green:#e2eee6;
  --tint-gold:#fcebd6;
}
*{margin:0;padding:0;box-sizing:border-box}
html,body{width:849px;height:1200px;overflow:hidden;background:var(--board)}
body{position:relative;font-family:"Fira Sans",Arial,sans-serif;color:var(--ink)}
.page{position:absolute;width:249px;height:352px;background:var(--paper);overflow:hidden;box-shadow:3px 4px 6px rgba(0,0,0,.45)}
.p-cover{left:169px;top:59px}
.p-about{left:430px;top:59px}
.p-format{left:169px;top:438px}
.p-audience{left:430px;top:438px}
.p-back{left:300px;top:812px}
.abs{position:absolute}
.brand{position:absolute;left:0;right:0;text-align:center;font-weight:600;color:var(--navy);font-size:5.2px;letter-spacing:.4px;line-height:6.5px;text-transform:uppercase}
.brand .mark{display:block;width:16px;height:16px;margin:4px auto 0;background:var(--navy)}
.photo{position:absolute}
.h-red{position:absolute;color:var(--red);font-style:italic;font-weight:600;font-size:7.2px;line-height:9px}
.h-blue{position:absolute;color:var(--blue);font-weight:600;font-size:5.4px;line-height:6.6px}
.txt{position:absolute;font-size:4.6px;line-height:6px;text-align:justify;color:var(--ink)}
.txt p+p{margin-top:5px}
.red{color:var(--red)}
.blue-i{color:var(--blue);font-style:italic}
.badge{position:absolute;border-radius:2px}
.badge-blue{background:var(--tint-blue)}
.badge-red{background:var(--tint-red)}
.badge-green{background:var(--tint-green)}
.badge-gold{background:var(--tint-gold)}
.ticks{position:absolute;list-style:none;font-size:4.6px;line-height:5.8px}
.ticks li{position:relative;padding-left:8px;margin-bottom:2.4px}
.ticks svg{position:absolute;left:0;top:.8px;width:4.6px;height:4.6px}
.arrows{position:absolute;list-style:none;font-size:3.9px;line-height:4.7px;color:#fff}
.arrows li{position:relative;padding-left:5px;margin-bottom:2.2px}
.arrows li::before{content:"";position:absolute;left:0;top:1.3px;border-left:2px solid #fff;border-top:1.3px solid transparent;border-bottom:1.3px solid transparent}
</style>
</head>
<body>

<!-- Cover -->
<section class="page p-cover">
  <div class="brand" style="top:27px">Harcourt Academy<br>of Learning<span class="mark"></span></div>
  <svg class="abs" style="left:89px;top:76px" width="70" height="9"><polygon points="0,9 35,0 70,9" fill="var(--navy)"/></svg>
  <div class="abs" style="left:0;top:89px;width:249px;height:3px;background:var(--navy)"></div>
  <div class="photo" role="img" aria-label="Care worker smiling and handing a glass of water to an elderly resident" style="left:0;top:92px;width:249px;height:166px;background:
    radial-gradient(ellipse 60px 50px at 50px 40px,#e6d8cf 0%,rgba(230,216,207,0) 100%),
    radial-gradient(ellipse 70px 90px at 55px 120px,#3f8fd0 0%,#5aa3dc 45%,rgba(90,163,220,0) 100%),
    radial-gradient(ellipse 30px 30px at 175px 45px,#7a4e38 0%,rgba(122,78,56,0) 100%),
    radial-gradient(ellipse 35px 35px at 175px 70px,#ecc9b1 0%,rgba(236,201,177,0) 100%),
    radial-gradient(ellipse 80px 70px at 195px 140px,#ffffff 0%,#f1f3f5 50%,rgba(241,243,245,0) 100%),
    linear-gradient(100deg,#b9c6d2 0%,#d8dee4 45%,#e9ecef 70%,#cfd6dd 100%)"></div>
  <div class="abs" style="left:0;top:258px;width:249px;height:3px;background:var(--navy)"></div>
  <svg class="abs" style="left:89px;top:264px" width="70" height="10"><polygon points="0,0 70,0 35,10" fill="var(--navy)"/></svg>
  <h1 class="abs" style="left:0;right:0;top:309px;text-align:center;font-weight:300;font-size:12.5px;color:#222">Infection Control – NEW!</h1>
  <div class="abs" style="left:98px;top:331px;width:53px;height:.7px;background:#333"></div>
</section>

<!-- About -->
<section class="page p-about">
  <h2 class="h-red" style="left:15px;top:14px">Infection Control Skill set<br>HCSS00218 for Health Care workers</h2>
  <div class="h-blue" style="left:15px;top:37px">HCINF204 - Comply with infection prevention and control policies and procedures</div>
  <div class="abs" style="left:0;top:49px;width:90px;height:76px;background:var(--mist)"></div>
  <div class="badge badge-red" style="left:14px;top:54px;width:43px;height:22px"></div>
  <div class="txt" style="left:15px;top:84px;width:70px;text-align:left;font-weight:600">Course cost</div>
  <div class="txt" style="left:15px;top:95px;width:69px">Free infection control skill sets for everyone in Western Australia or <span class="red">$350/for students outside of WA.</span></div>
  <div class="photo" role="img" aria-label="Cleaner in a face mask wiping a lift wall" style="left:90px;top:49px;width:154px;height:76px;background:
    radial-gradient(ellipse 14px 12px at 92px 12px,#e8c25a 0%,rgba(232,194,90,0) 100%),
    radial-gradient(ellipse 30px 30px at 55px 58px,#1d2f4d 0%,rgba(29,47,77,0) 100%),
    radial-gradient(ellipse 16px 14px at 122px 48px,#dfe4ea 0%,rgba(223,228,234,0) 100%),
    linear-gradient(100deg,#3d5f86 0%,#7ea4c9 30%,#a9c3de 50%,#5d82ab 75%,#2a4669 100%)"></div>
  <div class="photo" role="img" aria-label="Health worker adjusting safety glasses while wearing a mask, gloves and cap" style="left:0;top:130px;width:249px;height:84px;background:
    radial-gradient(ellipse 30px 26px at 55px 40px,#f4f4f4 0%,rgba(244,244,244,0) 100%),
    radial-gradient(ellipse 22px 30px at 20px 40px,#9c9fd6 0%,rgba(156,159,214,0) 100%),
    radial-gradient(ellipse 22px 30px at 92px 45px,#9c9fd6 0%,rgba(156,159,214,0) 100%),
    radial-gradient(ellipse 60px 20px at 55px 8px,#3e5f8a 0%,rgba(62,95,138,0) 100%),
    linear-gradient(90deg,#5d6670 0%,#8d9196 30%,#b7b7b7 55%,#8a8a8a 80%,#5e5e5e 100%)"></div>
  <div class="abs" style="left:128px;top:167px;font-size:5.2px;line-height:6.3px;color:#fff">Protect yourself and others in the<br>community from infectious diseases</div>
  <div class="abs" style="left:128px;top:181px;width:121px;height:.6px;background:#fff"></div>
  <div class="abs" style="left:0;top:214px;width:125px;height:138px;background:#f3f3f3"></div>
  <h2 class="h-red" style="left:15px;top:220px">About this course</h2>
  <div class="txt" style="left:15px;top:233px;width:107px">
    <p>There is not better time than now, to formally Upskill yourself and your team with a Nationally Accredited unit of Competency <span class="blue-i">in Infection Control prevention including the latest COVID19 infection control protocols (Health Standards Bureau).</span> Fast track your skills with Harcourt's Accredited Infection Control Skill set to get you job ready or enhance your current workplace skills.</p>
    <p>The COVID19 pandemic has highlighted the important of building the capacity and understanding of the workforce to <span class="red">practice safe infection control procedures.</span></p>
  </div>
  <div class="txt" style="left:127px;top:233px;width:107px">
    <p>This skill set will provide you with the skills and knowledge to assist in protecting yourself and others in the community from infectious diseases.</p>
    <p>You will understand how infections are spread, ways of preventing the spread of infection and how to protect yourself and others from infection.</p>
    <p style="padding-left:6px">The skill set is becoming increasingly important for all Health Care Workers – and all workers are encouraged to upskill themselves today, whether you are becoming Job Ready or for your professional development in Industry.</p>
  </div>
  <div class="photo" role="img" aria-label="Virus particle illustration" style="left:106px;top:309px;width:34px;height:34px;border-radius:50%;background:radial-gradient(circle at 40% 40%,#e4e4e4 0%,#b9b9b9 40%,#c83a32 70%,#8e1b17 100%)"></div>
</section>

<!-- Format and recognition -->
<section class="page p-format">
  <h2 class="h-red" style="left:15px;top:14px">Course format</h2>
  <div class="h-blue" style="left:15px;top:30px;width:108px">Online with face-to-face tutorial (in person or via Meetly)</div>
  <div class="badge badge-green" style="left:16px;top:51px;width:43px;height:33px"></div>
  <div class="txt" style="left:63px;top:50px;width:59px"><b>Our course is delivered to you online</b> which allows you to undertake study at your own pace. It is recommended completion occurs within a month.</div>
  <div class="txt" style="left:15px;top:92px;width:107px">
    <p>you have completed the <b>Online Component of your course,</b> you are invited into a <b>Practical Lab Session</b> via face to face learning; to practice skills and undertake a workplace simulated activity.</p>
    <p>Regional locations may be fulfilled by Meetly technology and Harcourt may also conduct on-site visits as required. Harcourt also travel to regional locations throughout the year. Group training sessions are also available for corporates and workplaces.</p>
  </div>
  <h2 class="h-red" style="left:15px;top:169px;width:108px">Mentor Support and Practical Sessions</h2>
  <div class="photo" role="img" aria-label="Hands in blue gloves forming a heart" style="left:15px;top:196px;width:107px;height:72px;background:
    radial-gradient(ellipse 34px 22px at 54px 36px,#6fa6e0 0%,#8dbbea 45%,rgba(141,187,234,0) 100%),
    radial-gradient(ellipse 20px 14px at 12px 64px,#e9c7b3 0%,rgba(233,199,179,0) 100%),
    radial-gradient(ellipse 20px 14px at 96px 64px,#e9c7b3 0%,rgba(233,199,179,0) 100%),
    linear-gradient(180deg,#cfd6de 0%,#e3e8ed 100%)"></div>
  <div class="txt" style="left:15px;top:277px;width:107px">Students are welcomed to the course by a short induction by your Tutor/Mentor to start you on your way with confidence! All of Harcourt's student resources, learner materials, videos are contained in Harcourt's easy to use LMS and learning is provided online at your convenience.</div>

  <h2 class="h-red" style="left:127px;top:14px">Industry Recognised</h2>
  <div class="txt" style="left:127px;top:28px;width:107px">Harcourt's unique program in Infection Control is supported by leading Industry bodies, and includes certification by the Health Standards Bureau, and other leading Health bodies in Australia. Our Unit of competency is Australian Recognised and Accredited.</div>
  <div class="badge badge-blue" style="left:135px;top:73px;width:92px;height:20px"></div>
  <div class="badge badge-blue" style="left:136px;top:103px;width:95px;height:11px"></div>
  <div class="badge badge-red" style="left:134px;top:132px;width:38px;height:24px"></div>
  <div class="badge badge-gold" style="left:186px;top:126px;width:27px;height:30px"></div>
  <div class="badge badge-red" style="left:134px;top:166px;width:46px;height:16px"></div>
  <div class="badge badge-gold" style="left:184px;top:166px;width:48px;height:16px"></div>

  <div class="abs" style="left:124px;top:196px;width:125px;height:156px;background:var(--mist)"></div>
  <h2 class="h-red" style="left:127px;top:202px;color:#333">Gain these skills:</h2>
  <ul class="ticks" style="left:127px;top:216px;width:107px">
    <li><svg viewBox="0 0 10 10"><rect x=".7" y=".7" width="8.6" height="8.6" fill="none" stroke="#333" stroke-width="1.2"/><path d="M2.5 5l2 2 3.5-4" fill="none" stroke="#333" stroke-width="1.3"/></svg>Gain Industry Certification in Hand Hygiene</li>
    <li><svg viewBox="0 0 10 10"><rect x=".7" y=".7" width="8.6" height="8.6" fill="none" stroke="#333" stroke-width="1.2"/><path d="M2.5 5l2 2 3.5-4" fill="none" stroke="#333" stroke-width="1.3"/></svg>Gain Industry Certification in COVID19 Infection Control</li>
    <li><svg viewBox="0 0 10 10"><rect x=".7" y=".7" width="8.6" height="8.6" fill="none" stroke="#333" stroke-width="1.2"/><path d="M2.5 5l2 2 3.5-4" fill="none" stroke="#333" stroke-width="1.3"/></svg>Gain Industry Certification in Cleaning, Disinfection and Sterilisation</li>
    <li><svg viewBox="0 0 10 10"><rect x=".7" y=".7" width="8.6" height="8.6" fill="none" stroke="#333" stroke-width="1.2"/><path d="M2.5 5l2 2 3.5-4" fill="none" stroke="#333" stroke-width="1.3"/></svg>Using personal protective equipment safely (practical session with complimentary PPE samples)</li>
    <li><svg viewBox="0 0 10 10"><rect x=".7" y=".7" width="8.6" height="8.6" fill="none" stroke="#333" stroke-width="1.2"/><path d="M2.5 5l2 2 3.5-4" fill="none" stroke="#333" stroke-width="1.3"/></svg>Understanding the chain of infection</li>
    <li><svg viewBox="0 0 10 10"><rect x=".7" y=".7" width="8.6" height="8.6" fill="none" stroke="#333" stroke-width="1.2"/><path d="M2.5 5l2 2 3.5-4" fill="none" stroke="#333" stroke-width="1.3"/></svg>Identify infection hazards and assess risks</li>
    <li><svg viewBox="0 0 10 10"><rect x=".7" y=".7" width="8.6" height="8.6" fill="none" stroke="#333" stroke-width="1.2"/><path d="M2.5 5l2 2 3.5-4" fill="none" stroke="#333" stroke-width="1.3"/></svg>How to prevent the spread and transmission of infection</li>
    <li><svg viewBox="0 0 10 10"><rect x=".7" y=".7" width="8.6" height="8.6" fill="none" stroke="#333" stroke-width="1.2"/><path d="M2.5 5l2 2 3.5-4" fill="none" stroke="#333" stroke-width="1.3"/></svg>Maintaining a clean work environment</li>
  </ul>
</section>

<!-- Audience and pathways -->
<section class="page p-audience">
  <div class="photo" role="img" aria-label="Smiling nurse in a white uniform in a clinic" style="left:0;top:0;width:133px;height:193px;background:
    radial-gradient(ellipse 22px 20px at 52px 10px,#d9b98a 0%,rgba(217,185,138,0) 100%),
    radial-gradient(ellipse 30px 36px at 55px 50px,#f0cdb5 0%,#e8c0a5 40%,rgba(232,192,165,0) 100%),
    radial-gradient(ellipse 55px 70px at 55px 150px,#ffffff 0%,#f4f6f8 55%,rgba(244,246,248,0) 100%),
    radial-gradient(ellipse 18px 24px at 118px 110px,#7aa8d6 0%,rgba(122,168,214,0) 100%),
    radial-gradient(ellipse 22px 30px at 115px 60px,#b9c9d8 0%,rgba(185,201,216,0) 100%),
    linear-gradient(160deg,#dde4ea 0%,#c7d2dc 45%,#e6e9ec 75%,#bccbd8 100%)"></div>
  <div class="abs" style="left:0;top:193px;width:249px;height:159px;background:var(--blue)"></div>
  <div class="abs" style="left:11px;top:124px;width:111px;height:209px;background:#fff;border-radius:4px"></div>
  <h2 class="h-red" style="left:15px;top:133px">Who this course is ideal for:</h2>
  <div class="txt" style="left:15px;top:147px;width:103px">The skill set course is most suitable for anyone working the healthcare sector, or those looking to entry employment in the health fields.</div>
  <div class="abs" style="left:15px;top:178px;width:103px;color:var(--blue);font-style:italic;font-weight:600;font-size:5.3px;line-height:6.5px">This training is for care workers across all health care settings, including:</div>
  <ul class="ticks" style="left:15px;top:199px;width:103px">
    <li><svg viewBox="0 0 10 10"><rect x=".7" y=".7" width="8.6" height="8.6" fill="none" stroke="#333" stroke-width="1.2"/><path d="M2.5 5l2 2 3.5-4" fill="none" stroke="#333" stroke-width="1.3"/></svg>Hospitals</li>
    <li><svg viewBox="0 0 10 10"><rect x=".7" y=".7" width="8.6" height="8.6" fill="none" stroke="#333" stroke-width="1.2"/><path d="M2.5 5l2 2 3.5-4" fill="none" stroke="#333" stroke-width="1.3"/></svg>Primary care</li>
    <li><svg viewBox="0 0 10 10"><rect x=".7" y=".7" width="8.6" height="8.6" fill="none" stroke="#333" stroke-width="1.2"/><path d="M2.5 5l2 2 3.5-4" fill="none" stroke="#333" stroke-width="1.3"/></svg>Medical practices, allied health, GP and specialist clinics</li>
    <li><svg viewBox="0 0 10 10"><rect x=".7" y=".7" width="8.6" height="8.6" fill="none" stroke="#333" stroke-width="1.2"/><path d="M2.5 5l2 2 3.5-4" fill="none" stroke="#333" stroke-width="1.3"/></svg>Aged care (both in residential aged care facilities or with visiting carers at home, including cleaners and cooks)</li>
    <li><svg viewBox="0 0 10 10"><rect x=".7" y=".7" width="8.6" height="8.6" fill="none" stroke="#333" stroke-width="1.2"/><path d="M2.5 5l2 2 3.5-4" fill="none" stroke="#333" stroke-width="1.3"/></svg>Disability (both in residential/shared care facilities or part-time carers in people's homes, including cleaners and cooks)</li>
    <li><svg viewBox="0 0 10 10"><rect x=".7" y=".7" width="8.6" height="8.6" fill="none" stroke="#333" stroke-width="1.2"/><path d="M2.5 5l2 2 3.5-4" fill="none" stroke="#333" stroke-width="1.3"/></svg>Allied health</li>
    <li><svg viewBox="0 0 10 10"><rect x=".7" y=".7" width="8.6" height="8.6" fill="none" stroke="#333" stroke-width="1.2"/><path d="M2.5 5l2 2 3.5-4" fill="none" stroke="#333" stroke-width="1.3"/></svg>Aboriginal Community Controlled Health Services</li>
    <li><svg viewBox="0 0 10 10"><rect x=".7" y=".7" width="8.6" height="8.6" fill="none" stroke="#333" stroke-width="1.2"/><path d="M2.5 5l2 2 3.5-4" fill="none" stroke="#333" stroke-width="1.3"/></svg>Pharmacies</li>
    <li><svg viewBox="0 0 10 10"><rect x=".7" y=".7" width="8.6" height="8.6" fill="none" stroke="#333" stroke-width="1.2"/><path d="M2.5 5l2 2 3.5-4" fill="none" stroke="#333" stroke-width="1.3"/></svg>Dental practices, including dentists, nurses, cleaners and receptionists</li>
  </ul>

  <h2 class="h-red" style="left:140px;top:14px;width:100px">Job opportunities and Study Pathways</h2>
  <div class="photo" role="img" aria-label="Collage of health care and cleaning workers on the job" style="left:140px;top:35px;width:92px;height:92px;background:
    radial-gradient(ellipse 24px 20px at 46px 46px,#e02a30 0%,rgba(224,42,48,.6) 50%,rgba(224,42,48,0) 100%),
    radial-gradient(ellipse 30px 30px at 20px 20px,#5d7fa8 0%,rgba(93,127,168,0) 100%),
    radial-gradient(ellipse 30px 30px at 72px 20px,#d7d0c8 0%,rgba(215,208,200,0) 100%),
    radial-gradient(ellipse 30px 30px at 20px 72px,#3e6494 0%,rgba(62,100,148,0) 100%),
    radial-gradient(ellipse 30px 30px at 72px 72px,#a37d6a 0%,rgba(163,125,106,0) 100%),
    linear-gradient(135deg,#6d87a8,#b8c4d1 50%,#7c93b0 100%)"></div>
  <div class="txt" style="left:140px;top:131px;width:94px">This course does not lead to a specific job outcome but will be helpful if you are, or would like to work in any of the areas described above. Our training course is designed to make students Job Ready or to enhance their job role.</div>
  <div class="txt" style="left:140px;top:172px;width:94px">The Units of Competency is a recognised Unit that can be used as a Credit Transfer in Qualifications such as:</div>
  <ul class="arrows" style="left:143px;top:204px;width:92px">
    <li>Certificate III Business Administration (Medical)</li>
    <li>Cert III and IV Health Administration</li>
    <li>Cert III in Individual Support (Aging, disability, home and community)</li>
    <li>Cert III in Allied Health Assistance</li>
    <li>Cert III/IV Dental Assisting</li>
    <li>Certificate III in Aboriginal and/or Torres Strait Islander Primary Health Care</li>
    <li>Cert II/III Community Services</li>
    <li>Certificate III in Cleaning Operations</li>
    <li>Cert II and III Health Support Services</li>
  </ul>
  <div class="abs" style="left:140px;top:291px;width:100px;font-size:4.6px;line-height:7.4px;color:#fff">More Qualifications that include this Unit of Competency can be found at<br><b>https://unitregistry.edu.au/units/details<br>HCINF204</b></div>
</section>

<!-- Back -->
<section class="page p-back">
  <div class="brand" style="top:242px">Harcourt Academy<br>of Learning<span class="mark"></span></div>
  <div class="abs" style="left:12px;top:303px;width:229px;height:1.6px;background:var(--blue)"></div>
  <div class="abs" style="left:0;right:0;top:309px;text-align:center;font-size:4.6px;line-height:8.5px;color:#222">
    <b>FREECALL :</b> 1800 472 913 | <b>WEBSITE:</b> www.harcourtlearning.edu.au | <b>E-MAIL:</b> info@harcourtlearning.edu.au<br>
    PO Box 4410, Riverside Park, Northgate DC, Perth, WA 6901 Australia | RTO 73846
  </div>
</section>

</body>
</html>
```